Meridale Cleaning Services

In need of a business card design suited for a growing cleaning company.

We offer our cleaning and maintenance services to a wide range of clients including but not limited to the following: constuction industry, hospitality, commercial, industrial and domestic

I want the card to be very noticable, i would like people to say 'hey, great card!' when i hand them my card.double sided would be nice

we want our business to come across as exceedingly professional and innovative (different).

a contemporary design is what we have in mind
we want to present an image of a quality business with a high standard of excellence in consistent service.

i just really need a card that persuades top end quality,
our business is very certified and also strives towards environmentaly friendly alternatives
Updates

hey sorry, i have uploaded my company logo design and name
cheers.

hey guys i have added my company logo/name file on my brief page. many thanks

sorry guys a typo in the brief..
address is Tolley Rd. not Tolly Rd
thanks

Industry/Entity Type

Industrial

Requirements
Must have
• company name: meridale cleaning services
operations manager: Colm Varetti
Tel: (02)9373 6204
Fax: (02)8645 7712
Mob: 0438571490

address: 47 Tolly RD Kelsby NSW 2084
Postal Adress: PO Box 5832 Norwen Vale NSW 2158
email: meridaleclean@wexanet.com.au
website: meridalecleaningservices.com.au

```html
<!DOCTYPE html>
<html lang="en">
<head>
<meta charset="utf-8">
<title>Meridale Cleaning Services – Business Card</title>
<link rel="stylesheet" href="https://fonts.googleapis.com/css2?family=Open+Sans:wght@400;600;700&display=swap">
<style>
  :root {
    --paper: #eef0f3;
    --paper-white: #ffffff;
    --streak-blue: rgba(70, 150, 215, 0.75);
    --streak-pale: rgba(180, 215, 240, 0.6);
    --streak-clear: rgba(255, 255, 255, 0);
    --brand-blue: #0d5bb5;
    --band-deep: #0577b8;
    --band-mid: #1aa6e3;
    --band-bright: #29d0fb;
    --text-light: #ffffff;
    --web-blue: #1b57a6;
  }
  * { margin: 0; padding: 0; box-sizing: border-box; }
  html, body { width: 1200px; height: 721px; overflow: hidden; background: var(--paper-white); }
  .card {
    position: relative;
    width: 1200px;
    height: 721px;
    overflow: hidden;
    font-family: "Open Sans", Arial, sans-serif;
    background: radial-gradient(ellipse at 55% 45%, var(--paper-white) 0%, var(--paper) 85%);
  }
  .streaks-top, .streaks-bottom { position: absolute; left: 0; width: 1200px; }
  .streaks-top {
    top: 0; height: 125px;
    background: linear-gradient(178deg, var(--streak-pale) 0%, var(--streak-blue) 25%, var(--streak-pale) 55%, var(--streak-clear) 100%);
  }
  .streaks-bottom {
    bottom: 0; height: 70px;
    background: linear-gradient(182deg, var(--streak-clear) 0%, var(--streak-pale) 45%, var(--streak-blue) 85%, var(--streak-pale) 100%);
  }
  .brand {
    position: absolute;
    left: 111px;
    top: 162px;
    display: flex;
    align-items: center;
    gap: 20px;
  }
  .brand-dot {
    width: 102px; height: 102px; border-radius: 50%;
    background: var(--brand-blue);
  }
  .brand-name {
    color: var(--brand-blue);
    font-weight: 700;
    line-height: 1;
  }
  .brand-name .lead { display: block; font-size: 60px; letter-spacing: -1px; }
  .brand-name .tail { display: block; font-size: 21px; margin-top: 4px; letter-spacing: 0.3px; }
  .band {
    position: absolute;
    left: 0; top: 294px;
    width: 1200px; height: 278px;
    background:
      radial-gradient(ellipse 420px 260px at 600px 110px, rgba(41,208,251,0.55), rgba(41,208,251,0) 70%),
      linear-gradient(90deg, var(--band-deep) 0%, var(--band-mid) 45%, var(--band-bright) 75%, var(--band-bright) 100%);
  }
  .contact { position: absolute; left: 230px; color: var(--text-light); line-height: 1; white-space: nowrap; }
  .person-name { top: 307px; font-size: 40px; font-weight: 600; letter-spacing: 0.2px; }
  .person-role { top: 340px; left: 228px; font-size: 25px; font-weight: 400; }
  .line { font-size: 27px; font-weight: 400; }
  .line.tel { top: 386px; }
  .line.fax { top: 414px; }
  .line.mob { top: 442px; }
  .line.email { top: 470px; }
  .address { font-size: 18px; font-weight: 400; }
  .address.street { top: 515px; }
  .address.postal { top: 536px; }
  .website {
    position: absolute;
    left: 232px; top: 604px;
    font-size: 21px;
    color: var(--web-blue);
    letter-spacing: 12.2px;
    white-space: nowrap;
    line-height: 1.2;
  }
</style>
</head>
<body>
  <main class="card">
    <div class="streaks-top" role="img" aria-label="Soft blue light streaks along the top edge"></div>
    <div class="streaks-bottom" role="img" aria-label="Soft blue light streaks along the bottom edge"></div>

    <div class="brand">
      <span class="brand-dot"></span>
      <span class="brand-name"><span class="lead">Meridale</span><span class="tail">CLEANING SERVICES</span></span>
    </div>

    <section class="band"></section>

    <h1 class="contact person-name">COLM VARETTI</h1>
    <p class="contact person-role">operations manager</p>
    <p class="contact line tel">Tel: (02)9373 6204</p>
    <p class="contact line fax">Fax: (02)8645 7712</p>
    <p class="contact line mob">Mob: 0438571490</p>
    <p class="contact line email">Email: meridaleclean@wexanet.com.au</p>
    <p class="contact address street">47 Tolley RD Kelsby NSW 2084</p>
    <p class="contact address postal">PO Box 5832 Norwen Vale NSW 2158</p>

    <p class="website">meridalecleaningservices.com.au</p>
  </main>
</body>
</html>
```